Private practice for psychiatry and psychotherapy needs a business card and logo

I need a logo and business card design for my private practice for psychiatry and psychotherapy. The optional names for my practice are: Vornhoute Praktijk voor Psychiatrie en Psychotherapie, or short: Praktijk Vornhoute.
I am a (child and adolescent) psychiatrist and psychotherapist. I diagnose and treat infants, children, adolescents and adults with psychiatric symptoms/disorders. I also give supervision to colleagues about their own treatments. My work is characterised by personal involvement, transparence, creativity and professionality.
I would like to have an appealing, light and bright, yet basic design that invites people (both children and adults) to contact me, gives trust and hope, without loosing professional appearance.
I uploaded my contact information which should not necessarily be all included (in this form) on the card as long as people know how to contact me. Please feel free to be creative!
Please note that my website is only temporarely and need a new design and update too!

Target Market(s)

Clients and patients (children, adolescents, adults) with psychiatric symptoms who need diagnosis and treatment. I work with private clients and patients through medical insurances.

Industry/Entity Type

Mental Health

Contact Information for Business Card

Dr. Sanne Vornhoute-ter Kuilen
Psychiater/Kinder- en Jeugdpsychiater
Wouter Heskampstraat 14
3071 PX Rotterdam
t: 06-51928764
e: info@praktijkvornhoute.nl
i: www.praktijkvornhoute.nl

Logo Text

Praktijk Vornhoute voor Psychiatrie en Psychotherapie; or short: Praktijk Vornhoute

Font styles to use
Sans Serif
Other font styles liked:
• up to designer

Requirements
Must have
• Appealing, light, bright, creative, trustful, professional and unique.

```html
<!DOCTYPE html>
<html lang="nl">
<head>
<meta charset="utf-8">
<title>Praktijk Vornhoute – visitekaartje</title>
<link rel="stylesheet" href="https://fonts.googleapis.com/css2?family=Roboto+Condensed:wght@300;400;700&display=swap">
<style>
  :root {
    --page: #ffffff;
    --card: #fbf0ea;
    --rose: #e84a76;
    --sky: #94d2db;
    --mint: #6bbfa6;
    --violet: #6e68ad;
    --navy: #244a70;
  }
  * { margin: 0; padding: 0; box-sizing: border-box; }
  html, body {
    width: 1200px; height: 621px; overflow: hidden;
    background: var(--page);
    font-family: "Roboto Condensed", "Arial Narrow", sans-serif;
    color: var(--rose);
  }
  .canvas { position: relative; width: 1200px; height: 621px; }
  .card {
    position: absolute; top: 159px;
    width: 472px; height: 305px;
    background: var(--card);
    overflow: hidden;
  }
  .card--front { left: 103px; }
  .card--back { left: 625px; }

  .color-band {
    position: absolute; left: 0; bottom: 0;
    width: 100%; height: 70px;
    background: linear-gradient(180deg, var(--sky) 0%, var(--violet) 45%, var(--navy) 80%);
  }

  .brand-mark {
    position: absolute; left: 55px; top: 95px;
    width: 60px; height: 60px; border-radius: 50%;
    background: var(--rose);
  }
  .brand-name {
    position: absolute; left: 153px; top: 96px;
    font-size: 27px; font-weight: 700; line-height: 1;
  }
  .owner-name {
    position: absolute; left: 153px; top: 138px;
    font-size: 18.5px; font-weight: 700; line-height: 1;
    white-space: nowrap;
  }
  .owner-name .title { font-weight: 300; }

  .contact-list { position: absolute; left: 0; top: 33px; width: 100%; list-style: none; }
  .contact-item {
    position: relative; height: 34px;
    font-size: 17.5px; font-weight: 700; line-height: 34px;
  }
  .contact-item svg { position: absolute; left: 102px; top: 8px; width: 17px; height: 17px; fill: var(--rose); }
  .contact-item .value { position: absolute; left: 139px; white-space: nowrap; }
  .contact-item--phone .value { left: 0; width: 472px; text-align: center; }
  .divider {
    position: absolute; left: 228px; top: 152px;
    width: 16px; height: 2px; background: var(--rose);
  }
  .address {
    position: absolute; left: 0; top: 170px; width: 472px;
    text-align: center; font-style: normal; line-height: 19px; font-size: 15px;
  }
  .address .role, .address .city { font-weight: 300; }
  .address .street { font-weight: 700; }
</style>
</head>
<body>
<main class="canvas">

  <section class="card card--front">
    <span class="brand-mark"></span>
    <h1 class="brand-name">Praktijk Vornhoute</h1>
    <p class="owner-name"><span class="title">Dr.</span> Sanne Vornhoute-ter Kuilen</p>
    <div class="color-band" role="img" aria-label="Kleurband in blauw, paars en donkerblauw"></div>
  </section>

  <section class="card card--back">
    <ul class="contact-list">
      <li class="contact-item contact-item--phone">
        <svg viewBox="0 0 24 24" aria-hidden="true"><path d="M6.6 10.8a15.1 15.1 0 0 0 6.6 6.6l2.2-2.2c.3-.3.7-.4 1-.2 1.1.4 2.3.6 3.6.6.6 0 1 .4 1 1V20c0 .6-.4 1-1 1A17 17 0 0 1 3 4c0-.6.4-1 1-1h3.5c.6 0 1 .4 1 1 0 1.3.2 2.5.6 3.6.1.3 0 .7-.2 1z"/></svg>
        <span class="value">06-51928764</span>
      </li>
      <li class="contact-item contact-item--email">
        <svg viewBox="0 0 24 24" aria-hidden="true"><path d="M2 5h20v14H2z"/><path d="M3 6.5 12 13l9-6.5" fill="none" stroke="var(--card)" stroke-width="1.5"/></svg>
        <span class="value">info@praktijkvornhoute.nl</span>
      </li>
      <li class="contact-item contact-item--web">
        <svg viewBox="0 0 24 24" aria-hidden="true"><circle cx="18" cy="5" r="3.2"/><circle cx="6" cy="12" r="3.2"/><circle cx="18" cy="19" r="3.2"/><path d="M6 12 18 5M6 12l12 7" stroke="var(--rose)" stroke-width="2"/></svg>
        <span class="value">www.praktijkvornhoute.nl</span>
      </li>
    </ul>
    <span class="divider"></span>
    <address class="address">
      <span class="role">Psychiater/kinder- en jeugdpsychiater</span><br>
      <span class="street">Wouter Heskampstraat 14</span><br>
      <span class="city">3071 PX Rotterdam</span>
    </address>
    <div class="color-band" role="img" aria-label="Kleurband in blauw, paars en donkerblauw"></div>
  </section>

</main>
</body>
</html>
```